Flyer-Design für 2-jährige Ausbildung in medizinischer Kosmetik gesucht
Tolle Designvorschläge, die gut die Vorgaben umgesetzt haben. Änderungswünsche und Fertigstellung erfolgten zügig und professionell. Unbedingt empfehlenswert.
Zielgruppe
2-jährige Vollzeitausbildung in Medizinische Kosmetik an einer Berufsfachschule in privater Trägerschaft (Schulgeld erforderlich, Förderung durch Bafög und der QZ möglich). Zielgruppe sind junge Frauen ab 16, die eine Ausbildung suchen.
Aufgabenstellung
Wir wünschen uns ein freches und modernes Design, das die 50-jährige Tradition der Privatschule und die klassische Schulausbildung aber trotzdem berücksichtigt.
Wünschenswert wäre die Einbindung eines zum Slogan passenden Bildes (Zeichnung oder Comics). Überwiegend in den Schulfarben gehalten (weiß, grün, grau/silber). Ein Plakat (DIN A 3) plus dazu passender Postkarte.

```html
<!DOCTYPE html>
<html lang="de">
<head>
<meta charset="utf-8">
<title>Havelstädter Fachschule für Hautpflege – Plakat</title>
<link rel="stylesheet" href="https://fonts.googleapis.com/css2?family=Roboto:wght@300;400;700&family=Lobster&display=swap">
<style>
  :root {
    --green: #6aab3f;
    --green-soft: #a9cf8c;
    --green-pale: #e6f1dc;
    --paper: #f7faf3;
    --ink: #54404a;
    --white: #ffffff;
  }
  * { margin: 0; padding: 0; box-sizing: border-box; }
  html, body { width: 872px; height: 1200px; overflow: hidden; }
  body {
    font-family: "Roboto", Arial, sans-serif;
    font-weight: 300;
    color: var(--ink);
    background: var(--paper);
  }
  .poster {
    position: relative;
    width: 872px;
    height: 1200px;
    overflow: hidden;
    background: linear-gradient(180deg, #eef6e6 0%, #fbfdf8 45%, #f1f7ea 100%);
  }
  .bg-circle {
    position: absolute;
    border-radius: 50%;
    background: var(--green-pale);
    opacity: .55;
  }
  .hero-art {
    position: absolute;
    left: 355px; top: 0;
    width: 517px; height: 390px;
    background: radial-gradient(ellipse at 55% 40%, #d9eef2 0%, #cfe8e6 35%, #e3f1da 65%, rgba(238,246,230,0) 100%);
  }
  .flower-art {
    position: absolute;
    left: 670px; top: 600px;
    width: 202px; height: 330px;
    background: radial-gradient(circle at 70% 40%, #9cc97c 0%, #b8da9f 45%, rgba(200,226,180,0) 75%);
  }
  .flower-art--small {
    left: 0; top: 1060px;
    width: 145px; height: 140px;
    background: radial-gradient(circle at 30% 70%, #e4e6dc 0%, rgba(228,230,220,0) 70%);
  }
  .brand {
    position: absolute;
    left: 51px; top: 128px;
    display: flex; align-items: center; gap: 14px;
  }
  .brand__mark {
    width: 112px; height: 112px;
    border-radius: 50%;
    background: var(--green);
    flex: none;
  }
  .brand__name {
    color: var(--green);
    font-weight: 700;
    font-size: 31px;
    line-height: 29px;
    text-transform: uppercase;
    letter-spacing: 1.5px;
  }
  .lead {
    position: absolute; left: 75px; top: 384px;
    font-size: 21px;
  }
  .branches {
    position: absolute; left: 75px; top: 436px;
    font-family: "Lobster", cursive;
    font-size: 46px;
    color: var(--green);
    white-space: nowrap;
  }
  .branches .sep { font-family: "Roboto", sans-serif; font-size: 26px; vertical-align: 8px; padding: 0 12px; color: var(--ink); }
  .intro {
    position: absolute; left: 75px; top: 568px;
    font-size: 18.5px; line-height: 29px;
  }
  .intro em { font-style: normal; color: var(--green); }
  .badge {
    position: absolute; left: 612px; top: 463px;
    width: 206px; height: 206px;
    border-radius: 50%;
    background: var(--green);
  }
  .dot-row {
    position: absolute; left: 0; top: 695px;
    display: flex; gap: 14px;
  }
  .dot-row span { width: 22px; height: 22px; border-radius: 50%; background: var(--green); }
  .start-label {
    position: absolute; left: 75px; top: 768px;
    font-size: 18.5px;
  }
  .start-date {
    position: absolute; left: 73px; top: 812px;
    font-family: "Lobster", cursive;
    font-size: 74px;
    color: var(--green);
  }
  .contact {
    position: absolute; top: 1043px;
    font-size: 17px; line-height: 26.5px;
    color: var(--green);
    font-weight: 400;
    font-style: normal;
  }
  .contact--address { left: 75px; }
  .contact--web { left: 486px; top: 1096px; }
  .dot-column {
    position: absolute; left: 412px; top: 1063px;
    display: flex; flex-direction: column; gap: 12px;
  }
  .dot-column span { width: 24px; height: 24px; border-radius: 50%; background: var(--ink); }
</style>
</head>
<body>
<main class="poster">
  <div class="bg-circle" style="left:130px;top:920px;width:230px;height:230px"></div>
  <div class="bg-circle" style="left:490px;top:930px;width:230px;height:230px"></div>
  <div class="bg-circle" style="left:290px;top:600px;width:200px;height:200px;opacity:.35"></div>

  <div class="hero-art" role="img" aria-label="Aquarell-Illustration eines Frauengesichts mit blauen und grünen Blüten"></div>
  <div class="flower-art" role="img" aria-label="Grünes Dahlien-Ornament"></div>
  <div class="flower-art flower-art--small" role="img" aria-label="Blasses Blüten-Ornament"></div>

  <div class="brand">
    <div class="brand__mark"></div>
    <div class="brand__name">Havelstädter<br>Fachschule<br>für<br>Hautpflege</div>
  </div>

  <p class="lead">Mit nur einer Ausbildung fit für drei Branchen:</p>
  <p class="branches">Beauty<span class="sep">•</span>Health<span class="sep">•</span>Wellness</p>

  <p class="intro">Seit 50 Jahren erfolgreich, bieten wir eine zweijährige<br>anspruchsvolle und qualifizierte Ausbildung zur<br><em>Medizinischen Kosmetikerin</em> an.</p>

  <div class="badge" role="img" aria-label="Siegel zur staatlichen Förderung"></div>

  <div class="dot-row"><span></span><span></span><span></span><span></span><span></span><span></span><span></span><span></span></div>

  <p class="start-label">Nächster Ausbildungsbeginn:</p>
  <p class="start-date">1.Oktober</p>

  <address class="contact contact--address">
    HFfH GmbH<br>
    Lindenhofweg 12, 10999 Berlin<br>
    T: 030/555 01 23<br>
    F: 030/555 01 24
  </address>

  <div class="dot-column"><span></span><span></span><span></span><span></span></div>

  <p class="contact contact--web">kontakt@hautpflege-fachschule.de<br>hautpflege-fachschule.de</p>
</main>
</body>
</html>
```